POOL BUILDING CONTRACTOR

our company has shifter focus over the past 18 month we no longer have a retail store and no longer clean pools we build concrete pools. our website if 5 years old we need a completely new site that shows our core product, building concrete pools & renovate concrete pools

here is a few of our competitors;
morvalpools.example
tenbrookpoolcrew.example
ridgelinewaterworksstudio.example
plungeduke.example
foremostbasinsandtubs.example
halbrinpoolsne.example

one we land on a final design I will upload customer before and after photos and any other content needed

Target Market(s)

People looking to build or renovate there pool

Industry/Entity Type

swimming pool

Coding

Coded - Design and coding required

Number of Pages Required

5+ page

Colors
0054AA
0677BA
7BADD7
CADEEF
E8F1F8

Requirements
Must have
• financing Service-Repairs & liners new build-photos renovate-remodeling design-consult customer-reviews Gallery Before-After Contact us 3D Design & Modeling construction process & Timeline Equipment Features Hardscapes I like these sites https://havenbasinsbyplan.example/ https://delmontipools.example/

```html
<!DOCTYPE html>
<html lang="en">
<head>
<meta charset="utf-8">
<title>Tidewell – Concrete Pool Builders</title>
<link rel="stylesheet" href="https://fonts.googleapis.com/css2?family=Fredoka:wght@500;600&family=Josefin+Sans:wght@300;400;600;700&display=swap">
<style>
:root{
  --cyan:#1fb3ea;
  --navy:#1c2a6e;
  --ink:#2c3a4b;
  --text:#6a7480;
  --slate:#4a5a78;
  --bg-soft:#f6f9fc;
  --line:#e4eaf0;
  --white:#ffffff;
}
*{box-sizing:border-box;margin:0;padding:0}
html,body{width:1200px;height:5319px;overflow:hidden}
body{position:relative;background:var(--white);font-family:"Josefin Sans",sans-serif;color:var(--text)}
.abs{position:absolute}
.btn{position:absolute;display:flex;align-items:center;justify-content:center;background:var(--cyan);color:#fff;font-weight:700;font-size:11px;letter-spacing:.3px;border-radius:3px;box-shadow:0 6px 14px rgba(31,179,234,.3);text-transform:uppercase}
.btn.light{background:#fff;color:var(--cyan)}
p.body{font-size:12.5px;line-height:23px;font-weight:300}

.site-header{position:absolute;left:0;top:0;width:1200px;height:78px;background:#fff;z-index:5}
.brand{position:absolute;left:120px;top:14px;display:flex;align-items:center;gap:8px}
.brand-dot{width:44px;height:44px;border-radius:50%;background:var(--cyan)}
.brand-name{font-family:"Fredoka",sans-serif;font-weight:600;font-size:34px;color:var(--navy);line-height:1}
.brand-tag{font-size:8px;color:var(--navy);letter-spacing:.4px;margin-top:2px}
.nav{position:absolute;top:29px;left:415px;font-size:14px;color:var(--ink)}
.nav a{position:absolute;white-space:nowrap;text-decoration:none;color:inherit}
.nav a.active{color:var(--cyan)}

.hero{position:absolute;left:0;top:78px;width:1200px;height:680px;background:linear-gradient(160deg,#5fd0f2 0%,#3aa8d8 35%,#2b86b5 65%,#4cc3ea 100%)}
.hero-title{position:absolute;left:118px;top:160px;font-family:"Fredoka",sans-serif;font-weight:600;font-size:54px;line-height:58px;color:#fff;letter-spacing:.5px}
.hero-copy{position:absolute;left:118px;top:358px;width:460px;font-size:15px;line-height:25px;color:#fff}

.stat{position:absolute;top:875px;width:215px;height:205px;background:#fff;box-shadow:0 8px 22px rgba(30,60,90,.12);text-align:center}
.stat svg{margin-top:32px}
.stat .num{font-family:"Fredoka",sans-serif;font-weight:500;font-size:30px;color:var(--ink);margin-top:14px}
.stat .lbl{font-size:12px;margin-top:6px}

.photo{position:absolute}
.exp-box{position:absolute;left:372px;top:1172px;width:228px;height:186px;background:var(--navy);color:#fff;text-align:center}
.exp-box .big{font-family:"Fredoka",sans-serif;font-weight:600;font-size:50px;margin-top:52px;line-height:1}
.exp-box .small{font-size:8px;font-weight:700;margin-top:6px}
.section-title{font-family:"Fredoka",sans-serif;font-weight:600;color:var(--ink)}

.offering{position:absolute;left:0;top:1797px;width:1200px;height:900px;background:var(--bg-soft)}
.svc{position:absolute;width:212px;background:#fff;box-shadow:0 8px 20px rgba(30,60,90,.1);padding:20px 20px 0}
.svc .pic{height:128px}
.svc h4{font-size:11px;font-weight:600;color:var(--ink);margin-top:24px;text-transform:uppercase}
.svc p{font-size:11.5px;line-height:22px;font-weight:300;margin-top:14px}
.svc .more{font-size:10.5px;font-weight:700;color:var(--ink);margin-top:14px;display:block}

.cta{position:absolute;left:0;top:2690px;width:1200px;height:450px;background:linear-gradient(180deg,#39b8e8 0%,#2a9bd0 50%,#47bfe9 100%)}

.quote-card{position:absolute;top:3345px;height:270px;background:#fff;box-shadow:4px 6px 0 #eef4f8;text-align:center}
.quote-card .mark{font-family:"Fredoka",sans-serif;font-size:70px;color:var(--cyan);line-height:1;margin-top:20px;height:52px}
.quote-card p{font-size:14px;line-height:25px;color:var(--text);padding:0 22px;margin-top:18px}
.person{position:absolute;top:3590px;width:140px;text-align:center}
.avatar{width:54px;height:54px;border-radius:50%;background:#c9d3dc;border:2px solid var(--slate);margin:0 auto}
.person .name{font-size:13px;font-weight:700;color:var(--ink);margin-top:8px}
.person .role{font-size:13px;color:var(--ink)}
.dot{position:absolute;width:8px;height:8px;border-radius:50%}

.contact-box{position:absolute;left:165px;top:4378px;width:920px;height:425px;background:#fff;box-shadow:0 10px 30px rgba(30,60,90,.1)}
.field{position:absolute;border:1px solid var(--line);background:#fafbfc;font-size:12px;color:var(--text);padding:14px 20px}
.acc{position:absolute;left:612px;width:418px;border:1px solid var(--line);background:#fff;font-size:10.5px;font-weight:700;color:var(--ink);padding:0 20px;display:flex;align-items:center;justify-content:space-between}

.footer h5{position:absolute;font-size:14px;font-weight:700;color:var(--ink)}
.footer ul{position:absolute;list-style:none;font-size:11px;color:var(--ink);font-weight:600;line-height:23px}
.footer .txt{position:absolute;font-size:13px;line-height:22px;color:var(--text)}
.social{position:absolute;top:5192px;width:26px;height:26px;border-radius:50%;border:1.5px solid var(--cyan)}
</style>
</head>
<body>

<header class="site-header">
  <div class="brand">
    <div class="brand-dot"></div>
    <div>
      <div class="brand-name">Tidewell</div>
      <div class="brand-tag">CONCRETE POOL BUILDERS</div>
    </div>
  </div>
  <nav class="nav">
    <a class="active" style="left:0">Home</a>
    <a style="left:70px">About</a>
    <a style="left:143px">Services</a>
    <a style="left:233px">Gallery</a>
    <a style="left:312px">Contact</a>
  </nav>
  <div class="btn" style="left:920px;top:20px;width:123px;height:38px">Get a Quote</div>
</header>

<section class="hero" role="img" aria-label="Backyard with a large new concrete pool beside a two-storey house">
  <h1 class="hero-title">BUILD YOUR<br>DREAM<br>BACKYARD</h1>
  <p class="hero-copy">We would love the opportunity to build the pool your family has always dreamt of. Our concrete pool builders design, build and renovate pools that bring your family joy for years.</p>
  <div class="btn" style="left:118px;top:487px;width:164px;height:43px">Get a Free Quote</div>
</section>
<svg class="abs" style="left:0;top:640px" width="1200" height="120" viewBox="0 0 1200 120" preserveAspectRatio="none">
  <path d="M0 80 C150 40 260 110 420 70 C560 35 640 90 780 70 C930 45 1050 20 1200 40 L1200 120 L0 120Z" fill="#bfe9f8" opacity=".7"/>
  <path d="M0 95 C180 70 300 115 470 88 C620 62 720 108 880 88 C1010 72 1110 60 1200 70 L1200 120 L0 120Z" fill="#fff"/>
</svg>

<div class="stat" style="left:130px">
  <svg width="52" height="44" viewBox="0 0 52 44" fill="none" stroke="#1fb3ea" stroke-width="2"><path d="M14 30V8a5 5 0 0110 0M30 30V8a5 5 0 0110 0M14 14h16M14 22h16M4 34c5-4 9 4 14 0s9 4 14 0 9 4 14 0M4 41c5-4 9 4 14 0s9 4 14 0 9 4 14 0"/></svg>
  <div class="num">8713</div><div class="lbl">Pools Built</div>
</div>
<div class="stat" style="left:370px">
  <svg width="52" height="48" viewBox="0 0 52 48" fill="none" stroke="#1fb3ea" stroke-width="2"><path d="M14 4h24v12a12 12 0 01-24 0zM14 8H6v4a8 8 0 008 8M38 8h8v4a8 8 0 01-8 8M26 28v8M18 36h16v8H18z"/></svg>
  <div class="num">15</div><div class="lbl">Years in Business</div>
</div>
<div class="stat" style="left:610px">
  <svg width="56" height="48" viewBox="0 0 56 48" fill="none" stroke="#1fb3ea" stroke-width="2"><circle cx="28" cy="10" r="6"/><circle cx="12" cy="18" r="5"/><circle cx="44" cy="18" r="5"/><path d="M18 44V28a10 10 0 0120 0v16M4 44V32a8 8 0 0114-4M52 44V32a8 8 0 00-14-4"/></svg>
  <div class="num">20+</div><div class="lbl">Experts</div>
</div>
<div class="stat" style="left:850px">
  <svg width="58" height="44" viewBox="0 0 58 44" fill="none" stroke="#1fb3ea" stroke-width="2"><path d="M4 10l10-4 8 6 10-4 8 6 12-4v26l-12 4-8-6-10 4-8-6-10 4z"/><circle cx="20" cy="20" r="3"/><circle cx="40" cy="24" r="3"/></svg>
  <div class="num">110+</div><div class="lbl">Locations</div>
</div>

<div class="photo" style="left:130px;top:1172px;width:230px;height:338px;background:linear-gradient(180deg,#2f5a33 0%,#4ab3d9 40%,#7fd6f2 100%)" role="img" aria-label="Curved concrete pool with tropical planting and loungers"></div>
<div class="photo" style="left:120px;top:1524px;width:240px;height:186px;background:linear-gradient(180deg,#3d6b3a 0%,#3aa9d4 50%,#6fd0ee 100%)" role="img" aria-label="Freeform concrete pool edged with plants"></div>
<div class="exp-box"><div class="big">50+</div><div class="small">YEARS EXPERIENCE</div></div>
<div class="photo" style="left:372px;top:1375px;width:228px;height:335px;background:linear-gradient(180deg,#a8c3d8 0%,#7a5a48 35%,#3ea7c6 65%,#9a8878 100%)" role="img" aria-label="Backyard pool with raised spa and timber fence"></div>

<h2 class="section-title abs" style="left:642px;top:1226px;font-size:34px">About Us</h2>
<p class="body abs" style="left:642px;top:1288px;width:400px">We build and renovate concrete pools, and nothing else. Every project starts with a design consult and a 3D model of your backyard, so you can see the pool, hardscapes and equipment before any digging begins. Our own crews handle the full build from excavation to the final finish.</p>
<p class="body abs" style="left:642px;top:1440px;width:400px">Have a tired pool? Our renovation team resurfaces, retiles and remodels concrete pools to look brand new. We also offer repairs, liners and flexible financing, and you can browse real before and after photos from our customers in the gallery.</p>
<div class="btn" style="left:642px;top:1611px;width:120px;height:37px">Learn More</div>

<section class="offering"></section>
<h2 class="section-title abs" style="left:118px;top:1922px;font-size:34px">What We're Offering</h2>
<p class="body abs" style="left:118px;top:1984px;width:480px">From the first consult to the first swim, we handle every step of building or renovating your concrete pool, with one team you can reach at any time.</p>
<p class="body abs" style="left:118px;top:2083px;width:480px">Our construction process follows a clear timeline: design and 3D modeling, permits, excavation, steel and plumbing, shotcrete, tile and coping, equipment, hardscapes and finish. You get weekly updates at every stage.</p>
<div class="btn" style="left:118px;top:2200px;width:160px;height:38px">View All Services</div>
<div class="photo" style="left:120px;top:2282px;width:480px;height:270px;border-radius:6px;background:linear-gradient(180deg,#b9c9d6 0%,#8a6f5a 40%,#4aa6c4 70%,#8f8a80 100%)" role="img" aria-label="Video still of a finished concrete pool and spa"></div>
<svg class="abs" style="left:318px;top:2376px" width="84" height="84" viewBox="0 0 84 84"><circle cx="42" cy="42" r="40" fill="rgba(255,255,255,.25)" stroke="#fff" stroke-width="3"/><path d="M34 28l22 14-22 14z" fill="#fff"/></svg>

<div class="svc" style="left:620px;top:1945px;height:300px">
  <div class="pic" style="background:linear-gradient(180deg,#9fb8cc,#4a9cc0 55%,#8b8275)" role="img" aria-label="New concrete pool build"></div>
  <h4>Concrete Pool Builds</h4><p>Custom concrete pools built from the ground up.</p><span class="more">LEARN MORE &#9656;</span>
</div>
<div class="svc" style="left:857px;top:1898px;height:325px">
  <div class="pic" style="background:linear-gradient(180deg,#8aa4b4,#2fa7dc 55%,#5fc4ea)" role="img" aria-label="Concrete pool being renovated"></div>
  <h4>Pool Renovation</h4><p>Resurfacing, retiling and full remodels.</p><span class="more">LEARN MORE &#9656;</span>
</div>
<div class="svc" style="left:620px;top:2262px;height:323px">
  <div class="pic" style="background:linear-gradient(160deg,#1e9fca,#5bc9ea 60%,#2e8fbb)" role="img" aria-label="3D model of a planned backyard pool"></div>
  <h4>3D Design &amp; Modeling</h4><p>See your pool in 3D before we break ground.</p><span class="more">LEARN MORE &#9656;</span>
</div>
<div class="svc" style="left:857px;top:2245px;height:322px">
  <div class="pic" style="background:linear-gradient(160deg,#0f4a8f,#2c72b8 60%,#1a5ba0)" role="img" aria-label="Finished pool at dusk"></div>
  <h4>Financing</h4><p>Flexible payment plans for your new pool.</p><span class="more">LEARN MORE &#9656;</span>
</div>

<section class="cta" role="img" aria-label="Poolside terrace with loungers under a cyan wash"></section>
<svg class="abs" style="left:0;top:2680px" width="1200" height="70" viewBox="0 0 1200 70" preserveAspectRatio="none">
  <path d="M0 0H1200V30C1080 10 1000 55 860 35 C720 15 640 55 480 38 C330 22 230 50 120 30 C70 22 30 28 0 35Z" fill="#f6f9fc"/>
</svg>
<div class="abs" style="left:0;top:2855px;width:1200px;text-align:center;color:#fff">
  <div style="font-size:10px;font-weight:700">Free Estimate</div>
  <div style="font-family:'Fredoka',sans-serif;font-weight:600;font-size:38px;margin-top:6px">Get A Free Design Consult</div>
  <div style="font-size:13px;line-height:23px;width:760px;margin:8px auto 0">Book a visit and we will measure your yard, talk through your ideas and prepare a 3D design with a clear price, timeline and financing options for your new pool.</div>
</div>
<div class="btn light" style="left:538px;top:3008px;width:124px;height:37px">Get a Quote</div>

<div class="abs" style="left:0;top:3238px;width:1200px;text-align:center">
  <div style="font-size:10px;color:var(--cyan);font-weight:600">Testimonial</div>
  <h2 class="section-title" style="font-size:34px;margin-top:6px">What Our Clients Say About Us?</h2>
</div>
<svg class="abs" style="left:42px;top:3440px" width="42" height="30" viewBox="0 0 42 30" fill="none" stroke="#1fb3ea" stroke-width="2"><path d="M40 15H2M16 1L2 15l14 14"/></svg>
<svg class="abs" style="left:1116px;top:3440px" width="42" height="30" viewBox="0 0 42 30" fill="none" stroke="#1fb3ea" stroke-width="2"><path d="M2 15h38M26 1l14 14-14 14"/></svg>
<div class="quote-card" style="left:140px;width:292px"><div class="mark">&ldquo;</div><p>The 3D design showed us exactly what we would get. The build stayed on schedule and the pool is perfect.</p></div>
<div class="quote-card" style="left:448px;width:312px"><div class="mark">&ldquo;</div><p>Our old pool was cracked and stained. After the renovation it looks brand new. Clear updates every week.</p></div>
<div class="quote-card" style="left:775px;width:310px"><div class="mark">&ldquo;</div><p>Financing made it possible to build this year. The crew was tidy, friendly and finished on time.</p></div>
<div class="person" style="left:205px"><div class="avatar" role="img" aria-label="Client portrait"></div><div class="name">Maren</div><div class="role">Happy Client</div></div>
<div class="person" style="left:530px"><div class="avatar" role="img" aria-label="Client portrait"></div><div class="name">Ilse Varga</div><div class="role">Happy Client</div></div>
<div class="person" style="left:854px"><div class="avatar" role="img" aria-label="Client portrait"></div><div class="name">Noor</div><div class="role">Happy Client</div></div>
<div class="dot" style="left:574px;top:3694px;background:var(--slate)"></div>
<div class="dot" style="left:592px;top:3694px;background:var(--cyan)"></div>
<div class="dot" style="left:610px;top:3694px;background:var(--slate)"></div>

<h2 class="section-title abs" style="left:0;top:3775px;width:1200px;text-align:center;font-size:34px">Before &amp; After Projects</h2>
<div class="photo" style="left:0;top:3868px;width:300px;height:298px;background:linear-gradient(180deg,#a9c3d6,#7a5a48 40%,#3ea7c6 70%,#8f8578)" role="img" aria-label="After: renovated pool with raised spa and fence"></div>
<div class="photo" style="left:300px;top:3868px;width:300px;height:298px;background:linear-gradient(180deg,#7fb2d8,#6a4a36 40%,#35b4e6 70%,#c9c1b2)" role="img" aria-label="After: new rectangular concrete pool beside a timber house"></div>
<div class="photo" style="left:600px;top:3868px;width:300px;height:298px;background:linear-gradient(180deg,#9dc6ea,#8f9aa6 45%,#3da5d6 75%,#a6a39a)" role="img" aria-label="After: large house with new pool, hardscapes and loungers"></div>
<div class="photo" style="left:900px;top:3868px;width:300px;height:298px;background:linear-gradient(180deg,#8fb4d0,#6f6a5e 40%,#5fa6ae 70%,#8a8276)" role="img" aria-label="Before: older pool and spa awaiting renovation"></div>
<div class="dot" style="left:566px;top:4194px;background:#cbe9f6"></div>
<div class="dot" style="left:584px;top:4194px;background:#cbe9f6"></div>
<div class="dot" style="left:602px;top:4194px;background:var(--cyan)"></div>
<div class="dot" style="left:620px;top:4194px;background:#cbe9f6"></div>

<div class="contact-box"></div>
<div class="field" style="left:220px;top:4392px;width:146px;height:42px">First Name</div>
<div class="field" style="left:390px;top:4392px;width:147px;height:42px">Last Name</div>
<div class="field" style="left:220px;top:4453px;width:146px;height:42px">Email Address</div>
<div class="field" style="left:390px;top:4453px;width:147px;height:42px">How can we help</div>
<div class="field" style="left:220px;top:4516px;width:317px;height:155px">Message</div>
<div class="btn" style="left:220px;top:4688px;width:120px;height:34px">Get a Quote</div>
<div class="acc" style="top:4378px;height:54px;background:var(--slate);color:#fff;border-color:var(--slate)">About Tidewell <span>&#8963;</span></div>
<div class="abs" style="left:612px;top:4432px;width:418px;height:104px;border:1px solid var(--line);border-top:none;padding:16px 20px;font-size:11.5px;line-height:22px">We design, build and renovate concrete pools. Every job includes a consult, a 3D model, a fixed timeline and optional financing.</div>
<div class="acc" style="top:4557px;height:50px">How long does a new pool build take? <span>&#8964;</span></div>
<div class="acc" style="top:4622px;height:50px">Do you offer financing? <span>&#8964;</span></div>
<div class="acc" style="top:4688px;height:50px">How does the construction process work? <span>&#8964;</span></div>

<footer class="footer">
  <div class="brand" style="top:5008px">
    <div class="brand-dot" style="width:52px;height:52px"></div>
    <div><div class="brand-name" style="font-size:40px">Tidewell</div><div class="brand-tag" style="font-size:9px">CONCRETE POOL BUILDERS</div></div>
  </div>
  <p class="txt" style="left:120px;top:5080px;width:230px">Concrete pool design, construction and renovation for your dream backyard.</p>
  <div class="social" style="left:120px"></div>
  <div class="social" style="left:157px"></div>
  <div class="social" style="left:194px"></div>
  <div class="social" style="left:231px"></div>

  <h5 style="left:407px;top:5024px">Quick Links</h5>
  <ul style="left:407px;top:5058px"><li>Home</li><li>About Us</li><li>Gallery</li><li>FAQ's</li><li>Process</li></ul>

  <h5 style="left:552px;top:5024px">Our Services</h5>
  <ul style="left:552px;top:5058px;line-height:26px"><li><span style="color:var(--cyan)">&rarr;</span> Concrete Pools</li><li><span style="color:var(--cyan)">&rarr;</span> Pool Renovation</li><li><span style="color:var(--cyan)">&rarr;</span> 3D Design</li><li><span style="color:var(--cyan)">&rarr;</span> Financing</li></ul>

  <h5 style="left:705px;top:5030px;font-size:15px">Working Hours</h5>
  <p class="txt" style="left:705px;top:5070px;line-height:26px">Mon - Fri: 08:00 - 18:00<br>Saturday: 09:00 - 14:00<br>Sunday: Close</p>

  <h5 style="left:900px;top:5030px;font-size:15px">Contact Us</h5>
  <p class="txt" style="left:900px;top:5076px;line-height:18px"><b style="color:var(--ink)">Email:</b><br>hello@tidewell.example</p>
  <p class="txt" style="left:900px;top:5124px;line-height:18px"><b style="color:var(--ink)">Phone:</b><br>+44 000 555 0147</p>
  <p class="txt" style="left:900px;top:5172px;line-height:18px"><b style="color:var(--ink)">Address:</b><br>12 Larch Row</p>
</footer>
<div class="abs" style="left:0;top:5299px;width:1200px;height:20px;background:var(--cyan)"></div>

</body>
</html>
```